Business Card Design

The image I attached was a quick thought to my design. I have triplets and was invisioning something with three figures with maybe the colors blue, pink and green. I would like it to look very chic and modern yet soothing/healing. I will take any fresh ideas as well.

Side 1: Contact Details
Side 2: Appointment section (mandatory)
Updates

Thank u all for your preliminary designs. I had sent the old design over and am looking for a bold fresh NEW LOOK  for CORE MOTION. I saw some really creative ideas in the gallery. If you have any other questions please feel free to email me at rtbwakes@quellmail.net.

Thanks

Please keep in mind that it is mandatory that on the back of the card is for appointments.

Thank you.

Reason: The two mandatory elements that need to be on the card is that her title needs to read as so:

Reason: The criteria is still not being met. Her title needs to read as so: Dr. Marisa Kettner, P.T., D.P.T. Doctor of Physical Therapy and The appointment info must go on the BACK of the card. Looking forward to some more great designs. Thanks.

Industry/Entity Type

Business

Contact Information for Business Card

Core Motion
Physical & Aquatic Therapy
Dr. Marisa Kettner, P.T., D.P.T.
Doctor of Physical Therapy

22-48 B Birchwick Lane
Elmbury, N.Y. 11592
(Located inside of the Summit gym in the Pinecrest shopping center)

Phone & Fax: (631) 555-0172
Mkettner4@harbornet.net

Requirements
Must have
• One the back I would like to do an appointment layout.

```html
<!DOCTYPE html>
<html lang="en">
<head>
<meta charset="utf-8">
<title>Core Motion – Business Card</title>
<link rel="stylesheet" href="https://fonts.googleapis.com/css2?family=Open+Sans:wght@400;600&family=Lato:wght@400;700;900&display=swap">
<style>
  :root {
    --stage: #ecebef;
    --card-white: #ffffff;
    --brand-pink: #e9398f;
    --brand-blue: #4a78bf;
    --text-blue: #3f5fa8;
    --rule-grey: #c9c9cc;
    --white: #ffffff;
    --white-soft: rgba(255,255,255,0.75);
  }
  * { box-sizing: border-box; margin: 0; padding: 0; }
  html, body {
    width: 1200px; height: 900px; overflow: hidden;
    background: var(--stage);
  }
  .stage {
    position: relative; width: 1200px; height: 900px;
    display: flex; align-items: center; justify-content: center; gap: 50px;
  }
  .card {
    position: relative; width: 540px; height: 310px;
    box-shadow: 0 6px 18px rgba(0,0,0,0.18);
    overflow: hidden;
  }

  /* Front: contact details */
  .card-front { background: var(--card-white); font-family: "Open Sans", sans-serif; }
  .front-band {
    position: absolute; left: 40px; top: 34px; width: 460px; height: 102px;
    background: var(--brand-pink);
    display: flex; align-items: center; justify-content: space-between;
    padding: 0 28px 0 0;
  }
  .front-mark {
    height: 100%; display: flex; align-items: center; gap: 10px;
    background: var(--brand-blue); padding: 0 16px;
  }
  .front-mark .mark-square { width: 16px; height: 16px; background: var(--white); }
  .front-mark .mark-name { color: var(--white); font-weight: 600; font-size: 15px; }
  .front-title {
    color: var(--brand-blue); font-size: 30px; font-weight: 400; letter-spacing: 2px;
  }
  .rule { position: absolute; left: 40px; width: 460px; height: 1px; background: var(--rule-grey); }
  .rule-top { top: 146px; }
  .rule-bottom { top: 298px; }
  .contact-list {
    position: absolute; left: 40px; top: 156px; width: 262px;
    list-style: none; color: var(--text-blue); font-size: 11.5px; line-height: 1.25;
  }
  .contact-item { display: flex; gap: 14px; align-items: flex-start; }
  .contact-item + .contact-item { margin-top: 12px; }
  .contact-item.phone, .contact-item.mail { align-items: center; }
  .contact-icon { flex: 0 0 26px; width: 26px; height: 26px; }
  .divider {
    position: absolute; left: 312px; top: 160px; width: 1px; height: 110px; background: var(--rule-grey);
  }
  .role-list {
    position: absolute; left: 326px; top: 162px;
    list-style: none; color: var(--text-blue); font-size: 12.5px;
  }
  .role-list li + li { margin-top: 18px; }

  /* Back: appointment side */
  .card-back {
    background: var(--brand-pink); font-family: "Lato", sans-serif; color: var(--white);
  }
  .back-mark {
    position: absolute; left: 0; right: 0; top: 22px;
    display: flex; flex-direction: column; align-items: center; gap: 6px;
  }
  .back-mark .mark-square { width: 34px; height: 34px; background: var(--brand-blue); }
  .back-mark .mark-name { font-size: 17px; font-weight: 700; }
  .back-rule { position: absolute; left: 34px; width: 472px; height: 1px; background: var(--white); }
  .back-rule-top { top: 100px; }
  .back-rule-bottom { top: 156px; }
  .back-title {
    position: absolute; left: 0; right: 0; top: 108px; text-align: center;
    font-size: 26px; font-weight: 900; letter-spacing: 0.2px; line-height: 1.2;
  }
  .back-name {
    position: absolute; left: 0; right: 0; top: 141px; text-align: center;
    font-size: 9px; font-weight: 400; letter-spacing: 0.3px;
  }
  .appointment {
    position: absolute; left: 34px; top: 170px; width: 472px;
  }
  .appointment-heading {
    font-size: 12px; font-weight: 700; letter-spacing: 2px; text-align: center;
    margin-bottom: 10px;
  }
  .appointment-row {
    display: flex; gap: 18px; margin-bottom: 14px;
  }
  .appointment-field {
    flex: 1; display: flex; align-items: flex-end; gap: 8px;
    font-size: 11px; font-weight: 400;
  }
  .appointment-field .field-line {
    flex: 1; height: 1px; background: var(--white-soft); margin-bottom: 3px;
  }
</style>
</head>
<body>
<main class="stage">

  <section class="card card-front" aria-label="Front of card: contact details">
    <div class="front-band">
      <div class="front-mark">
        <span class="mark-square"></span>
        <span class="mark-name">Core Motion</span>
      </div>
      <h1 class="front-title">Core Motion</h1>
    </div>
    <div class="rule rule-top"></div>

    <ul class="contact-list">
      <li class="contact-item address">
        <svg class="contact-icon" viewBox="0 0 26 26" aria-hidden="true">
          <circle cx="13" cy="13" r="13" fill="var(--brand-blue)"/>
          <path d="M6.5 13.5 L13 7.5 L19.5 13.5 H17.5 V19 H14.5 V15.5 H11.5 V19 H8.5 V13.5 Z" fill="var(--white)"/>
        </svg>
        <span>22-48 B Birchwick Lane<br>Elmbury, N.Y. 11592<br>(Located inside of the Summit<br>gym in the Pinecrest shopping center)</span>
      </li>
      <li class="contact-item phone">
        <svg class="contact-icon" viewBox="0 0 26 26" aria-hidden="true">
          <circle cx="13" cy="13" r="13" fill="var(--brand-blue)"/>
          <path d="M7 11 Q13 6 19 11 L17.5 12.5 L15.5 11.5 V10.5 Q13 9.5 10.5 10.5 V11.5 L8.5 12.5 Z" fill="var(--white)"/>
          <rect x="9" y="13" width="8" height="5.5" rx="1" fill="var(--white)"/>
        </svg>
        <span>(631) 555-0172</span>
      </li>
      <li class="contact-item mail">
        <svg class="contact-icon" viewBox="0 0 26 26" aria-hidden="true">
          <circle cx="13" cy="13" r="13" fill="var(--brand-blue)"/>
          <rect x="7" y="8.5" width="12" height="9" fill="var(--white)"/>
          <path d="M7 8.5 L13 13.5 L19 8.5" fill="none" stroke="var(--brand-blue)" stroke-width="1.2"/>
        </svg>
        <span>Mkettner4@harbornet.net</span>
      </li>
    </ul>

    <div class="divider"></div>
    <ul class="role-list">
      <li>Physical &amp; Aquatic Therapy</li>
      <li>Dr. Marisa Kettner, P.T., D.P.T.</li>
      <li>Doctor of Physical Therapy</li>
    </ul>
    <div class="rule rule-bottom"></div>
  </section>

  <section class="card card-back" aria-label="Back of card: appointments">
    <div class="back-mark">
      <span class="mark-square"></span>
      <span class="mark-name">Core Motion</span>
    </div>
    <div class="back-rule back-rule-top"></div>
    <h2 class="back-title">PHYSICAL &amp; AQUATIC THERAPY</h2>
    <p class="back-name">DR MARISA KETTNER, P.T., D.P.T.</p>
    <div class="back-rule back-rule-bottom"></div>

    <div class="appointment">
      <p class="appointment-heading">YOUR NEXT APPOINTMENT</p>
      <div class="appointment-row">
        <span class="appointment-field">Date<span class="field-line"></span></span>
        <span class="appointment-field">Time<span class="field-line"></span></span>
      </div>
      <div class="appointment-row">
        <span class="appointment-field">Date<span class="field-line"></span></span>
        <span class="appointment-field">Time<span class="field-line"></span></span>
      </div>
      <div class="appointment-row">
        <span class="appointment-field">Date<span class="field-line"></span></span>
        <span class="appointment-field">Time<span class="field-line"></span></span>
      </div>
    </div>
  </section>

</main>
</body>
</html>
```